a Label for a candle jar and its gift box

I would like a label that is modern minimalist for candles jars. These jars are colored as white, amber and black. I am thinking maybe foiling gold/silver background with logo only and maybe company name in different color that suits the foiling background color/s. I would like a high quality luxurious design that shows the preciousness of this candle. I am open to any ideas you might have for the design but so far I have used a logo only on the jar which I really like BUT I still feel that it is not enough branding for people when you only show them the logo so I am considering adding the business name. Again, I am open to both ideas (with logo only or logo with business name (Velvet Lantern).

IMPORTANT: YOU MAY IGNORE MY DESIGN COMPLETELY AND DO YOUR OWN ONE AS LONG AS YOU KERP THE LOGO DESIGN. YOU MAY ALSO ADJUST THE LOGO A BIT TO SUIT YOUR DESIGN. - sorry im using capital letters to show importance but im not yelling :)
Updates

UPDATE: To clarify, I have uploaded a video called Corvale in the box to show what the current product look like. It is a corvale jar with a logo only and the jar box has a window that shows the jar with the logo on it and the back of that jar box has a bigger version of the label that has more details (i.e. Fragrance name and website link). So to make it clear, I would like to have two versions of the lables: 1. on the jar with minimal info (logo only or logo with the business name) 2. Bigger version of the label with more info to put on the back of the jar box - as described above. The dimensions of the jars are as per this link https://www.plintova.com.au/corvale-medium-base-and-flat-lid-amber-packed-with-lid-on/ The dimensions of the jar box as per this link https://www.plintova.com.au/corvale-medium-flat-lid-candle-box-with-window-beige/ Looking forward to some artistic productions :)

Update #2: Tues 25 Dec 18 1. I have uploaded the photo which has the logo with the name 'Velvet Lantern' below it just for a reference. However, I would like the designer to modify the current font and NOT to use it as the word 'of in the phrase 'Velvet Lantern' does not come out clear enough after printing. 2. I would like the designer NOT to create a design that will require a clear sticker/label for printing. 3. I have attached the photos of my current designs on the jars or the jar box just as a reference but please do NOT just use the same fonts and only change background. I am hoping to see something different and more professional than my own design :) Thank you very much!

Font styles to use
Decorative
Script

Requirements
Must have
• I would like them to fit on the three colors of the jars below - white, amber and black. Below is a link to how the jar looks like https://www.plintova.com.au/candle-making-supplies/candle-jars/corvale-candle-jars/?glassware_colour=415,443,417&glassware_size=268
Nice to have
• I would like to have a modern design which is suitable for both feminine and musculine.
Should not have
• shouldnt have so much writing on it!

```html
<!DOCTYPE html>
<html lang="en">
<head>
<meta charset="utf-8">
<title>Velvet Lantern – Jar Label and Gift Box Dieline</title>
<link rel="stylesheet" href="https://fonts.googleapis.com/css2?family=Cinzel:wght@400;500&family=Montserrat:wght@400;500&display=swap">
<style>
  :root {
    --canvas-bg: #f4f1ee;
    --box-black: #0b0b0b;
    --panel-white: #ffffff;
    --ink: #1c1c1c;
    --label-gold: #f0b62c;
    --wreath-gold: #f5c95a;
    --wreath-light: #ececec;
    --wreath-dark: #2a2a2a;
    --label-text: #ffffff;
  }
  html, body {
    margin: 0;
    padding: 0;
    width: 1200px;
    height: 1199px;
    overflow: hidden;
    background: var(--canvas-bg);
  }
  .artboard {
    display: block;
    width: 1200px;
    height: 1199px;
  }
  .brand-name {
    font-family: "Cinzel", serif;
    font-weight: 400;
    letter-spacing: 0.02em;
  }
  .fragrance-name {
    font-family: "Cinzel", serif;
    font-weight: 500;
    letter-spacing: 0.12em;
  }
  .contact-line {
    font-family: "Montserrat", sans-serif;
    font-weight: 500;
  }
</style>
</head>
<body>
<svg class="artboard" viewBox="0 0 1200 1199" xmlns="http://www.w3.org/2000/svg">

  <!-- Round jar label -->
  <g class="jar-label">
    <circle cx="600" cy="340" r="200" fill="var(--label-gold)"/>
    <circle class="wreath" role="img" aria-label="Ornamental scroll wreath framing the brand name"
            cx="600" cy="340" r="165" fill="none" stroke="var(--wreath-gold)" stroke-width="46"/>
    <g class="label-text" fill="var(--label-text)" text-anchor="middle">
      <circle cx="600" cy="262" r="6"/>
      <text class="brand-name" x="600" y="330" font-size="40">VELVET</text>
      <text class="brand-name" x="600" y="378" font-size="40">LANTERN</text>
    </g>
  </g>

  <!-- Gift box dieline -->
  <g class="box-dieline">
    <path class="lid-flap" d="M162 876 V720 Q162 696 186 696 H358 Q382 696 382 720 V876 Z" fill="var(--box-black)"/>
    <rect class="side-strip" x="162" y="876" width="876" height="292" fill="var(--box-black)"/>

    <rect class="panel panel-back" x="171" y="886" width="203" height="270" fill="var(--panel-white)"/>
    <rect class="panel panel-side" x="392" y="886" width="198" height="270" fill="var(--panel-white)"/>
    <rect class="panel panel-window" x="634" y="910" width="152" height="225" fill="var(--panel-white)"/>
    <rect class="panel panel-side" x="832" y="886" width="196" height="270" fill="var(--panel-white)"/>

    <!-- Lid flap logo, printed upside down -->
    <g class="lid-logo" transform="rotate(180 271 800)">
      <circle role="img" aria-label="Ornamental scroll wreath" cx="271" cy="800" r="52"
              fill="none" stroke="var(--wreath-dark)" stroke-width="14"/>
      <g fill="var(--label-text)" text-anchor="middle">
        <circle cx="271" cy="772" r="2.5"/>
        <text class="brand-name" x="271" y="798" font-size="13">VELVET</text>
        <text class="brand-name" x="271" y="815" font-size="13">LANTERN</text>
        <text class="fragrance-name" x="271" y="828" font-size="5">TURKISH ROSE</text>
      </g>
    </g>

    <!-- Back panel label with details -->
    <g class="back-label">
      <circle role="img" aria-label="Ornamental scroll wreath" cx="271" cy="1025" r="70"
              fill="none" stroke="var(--wreath-light)" stroke-width="18"/>
      <g fill="var(--ink)" text-anchor="middle">
        <circle cx="271" cy="985" r="3"/>
        <text class="brand-name" x="271" y="1022" font-size="18">VELVET</text>
        <text class="brand-name" x="271" y="1044" font-size="18">LANTERN</text>
        <text class="fragrance-name" x="271" y="1059" font-size="6.5">— TURKISH ROSE —</text>
        <text class="contact-line" x="271" y="1126" font-size="6">+61 455 218 903  |  info@velvetlantern.com.au</text>
        <text class="contact-line" x="271" y="1137" font-size="6" letter-spacing="1.6">www.velvetlantern.com.au</text>
      </g>
    </g>
  </g>

</svg>
</body>
</html>
```